Award winning Indie press looking for a world class book cover for global relaunch

We need to update a book cover for one of our titles which is being relaunched. The title will exist in both physical and e-formats.
There are two primary targets for this book:
1- the coming of age story coupled with the element of forbidden love between a local boy and a British girl
2- the political division of a British colony in the 1950's
Size: A5
Spine: .777 inches or 19.73mm
Title: Hither and Yonder (you may substitute 'and' with '&')
Author: Evangelos K. Drakoulides
Translated by Helen Marsh-Tolley
Blurb: You see before you the entire social mosaic of Cyprus in the ‘50s. - Proinopistis
Publisher: logo- provided
Back cover text:
The touching story of a teenager who struggles with the eternal problems of adolescence, Hither & Yonder is a coming-of-age novel set in a politically divided country.
While the era of British colonialism in Cyprus is coming to a violent end, Dimitri tries to come to terms with the consequences of the political turmoil on his own life. Strengthened by his passion for medieval poetry and his love for the history of his island, he sets out to balance the Cypriot and English elements in his daily life. His quest for answers is complicated by romantic love for his British friend Anne and his physical attraction to his father’s maid Phrossou. Balancing between different identities, religion and communities, his personal search becomes symbolic of his country’s turbulent political situation.
A nostalgic story about family, love and friendship, Hither & Yonder is a powerful novel about the psychology of an adolescent torn between different worlds, and about the complexities of life and love in the social and historical mosaic of 1950’s colonial Cyprus. It is a beautifully-observed, historically-informed novel by the celebrated Greek historian and novelist.
Other: Please allow a box of approximately 2cm height X 3 cm length for the bar code.
Updates
Hi
I've added two images that could be of some help to you.
Hope they help.
Reason: Appreciating the specific difficulties of this design, it's best to have a few more days
Hi
Please amend front cover blurb to the following:
"This is a novel to be read in one go. A charming narrative…and unexpected turns. It keeps the reader in constant suspense". Grafima Monthly Literary Review
Target Market(s)
1 - Adults reading coming of age novels
2 - Adults reading historical fiction on British colonialism
Industry/Entity Type
Political
Colors
Designer to choose colors to be used in the design.
Look and feel
Each slider illustrates characteristics of the customer's brand and the style your logo design should communicate.

```html
<!DOCTYPE html>
<html lang="en">
<head>
<meta charset="utf-8">
<title>Hither &amp; Yonder — Cover Spread</title>
<link rel="stylesheet" href="https://fonts.googleapis.com/css2?family=PT+Serif:ital,wght@0,400;0,700;1,400&family=Open+Sans:ital,wght@0,400;0,700;1,400&display=swap">
<style>
  :root {
    --stage: #f2f2f0;
    --paper: #dcc892;
    --paper-light: #eadbb0;
    --paper-edge: #c9b178;
    --spine: #c8ae73;
    --ink: #3a332a;
    --ink-soft: #4a4236;
    --rule: #3a332a;
    --frame: #f7f3ea;
    --sepia-dark: #4b3f2f;
    --sepia-mid: #8a7659;
    --sepia-light: #c9b896;
  }
  * { box-sizing: border-box; margin: 0; padding: 0; }
  html, body { width: 1200px; height: 1200px; overflow: hidden; }
  body { background: var(--stage); font-family: "Open Sans", sans-serif; color: var(--ink); }

  .spread {
    position: absolute; left: 40px; top: 227px;
    width: 1120px; height: 745px;
    display: flex;
    box-shadow: 0 6px 24px rgba(0,0,0,.18);
  }
  .panel {
    position: relative; height: 100%;
    background: radial-gradient(ellipse at 50% 35%, var(--paper-light) 0%, var(--paper) 60%, var(--paper-edge) 100%);
  }
  .back-cover { width: 525px; padding: 48px 40px 0 40px; }
  .spine {
    width: 70px;
    background: linear-gradient(90deg, var(--paper-edge), var(--spine) 50%, var(--paper-edge));
  }
  .front-cover { width: 525px; text-align: center; }

  /* Back cover */
  .back-title {
    font-family: "PT Serif", serif; font-weight: 400;
    font-size: 50px; line-height: 1; color: var(--ink);
  }
  .back-title .line-two { display: block; padding-left: 2px; }
  .back-rule { height: 2px; background: var(--rule); margin: 14px 0 14px; }
  .back-copy p {
    font-size: 11.3px; line-height: 1.55; color: var(--ink-soft);
    margin-bottom: 18px;
  }
  .back-footer-rule { position: absolute; left: 40px; right: 40px; bottom: 142px; height: 2px; background: var(--rule); }
  .barcode-space {
    position: absolute; right: 48px; bottom: 28px;
    width: 106px; height: 71px; background: #fff;
  }

  /* Publisher name */
  .imprint {
    position: absolute; bottom: 36px;
    font-family: "PT Serif", serif; font-weight: 400;
    font-size: 17px; color: var(--ink);
    white-space: nowrap;
  }
  .back-cover .imprint { left: 40px; }
  .front-cover .imprint { left: 50%; transform: translateX(-50%); }

  /* Spine */
  .spine-text {
    position: absolute; left: 0; top: 0; width: 100%; height: 100%;
    writing-mode: vertical-rl;
    font-family: "PT Serif", serif; color: var(--ink);
  }
  .spine-title { font-size: 30px; position: absolute; top: 34px; left: 50%; transform: translateX(-50%); white-space: nowrap; }
  .spine-credits {
    position: absolute; top: 418px; left: 50%; transform: translateX(-50%);
    font-size: 15px; line-height: 1.45; white-space: nowrap; text-align: left;
  }

  /* Front cover */
  .credits {
    padding-top: 30px;
    font-family: "PT Serif", serif; font-weight: 700;
    font-size: 20px; line-height: 1.22; color: var(--ink);
  }
  .credits-rule { display: block; margin: 12px auto 0; }
  .front-title {
    margin-top: 22px;
    font-family: "PT Serif", serif; font-weight: 400;
    font-size: 66px; line-height: 1; color: var(--ink-soft);
  }
  .front-title .line-one { display: block; }
  .front-title .line-two { display: block; margin-top: 2px; padding-left: 16px; }
  .scene-windows { display: block; margin: 20px auto 0; }
  .praise {
    margin-top: 14px;
    font-family: "Open Sans", sans-serif; font-size: 16.5px; line-height: 1.3; color: var(--ink);
  }
  .praise-source {
    margin-top: 6px; padding-right: 92px; text-align: right;
    font-style: italic; font-size: 15px; color: var(--ink);
  }
</style>
</head>
<body>
  <main class="spread">
    <section class="panel back-cover">
      <h2 class="back-title">Hither<span class="line-two">&amp; Yonder</span></h2>
      <div class="back-rule"></div>
      <div class="back-copy">
        <p>The touching story of a teenager who struggles with the eternal problems of adolescence, Hither &amp; Yonder is a coming-of-age novel set in a politically divided country.</p>
        <p>While the era of British colonialism in Cyprus is coming to a violent end, Dimitri tries to come to terms with the consequences of the political turmoil on his own life. Strengthened by his passion for medieval poetry and his love for the history of his island, he sets out to balance the Cypriot and English elements in his daily life. His quest for answers is complicated by romantic love for his British friend Anne and his physical attraction to his father’s maid Phrossou. Balancing between different identities, religion and communities, his personal search becomes symbolic of his country’s turbulent political situation.</p>
        <p>A nostalgic story about family, love and friendship, Hither &amp; Yonder is a powerful novel about the psychology of an adolescent torn between different worlds, and about the complexities of life and love in the social and historical mosaic of 1950’s colonial Cyprus. It is a beautifully-observed, historically-informed novel by the celebrated Greek historian and novelist.</p>
      </div>
      <div class="back-footer-rule"></div>
      <div class="imprint">Quillstone Books</div>
      <div class="barcode-space"></div>
    </section>

    <section class="panel spine">
      <div class="spine-text">
        <span class="spine-title">Hither &amp; Yonder</span>
        <span class="spine-credits">Evangelos K. Drakoulides<br>Translated by Helen Marsh-Tolley</span>
      </div>
    </section>

    <section class="panel front-cover">
      <div class="credits">
        Evangelos K. Drakoulides<br>Translated by Helen Marsh-Tolley
        <svg class="credits-rule" width="330" height="10" viewBox="0 0 330 10" aria-hidden="true">
          <line x1="5" y1="5" x2="325" y2="5" stroke="var(--rule)" stroke-width="2"/>
          <circle cx="5" cy="5" r="4" fill="var(--rule)"/>
          <circle cx="325" cy="5" r="4" fill="var(--rule)"/>
        </svg>
      </div>
      <h1 class="front-title"><span class="line-one">Hither</span><span class="line-two">&amp; Yonder</span></h1>
      <svg class="scene-windows" width="250" height="226" viewBox="0 0 250 226" role="img" aria-label="Sepia photograph of an old bicycle leaning against a stone wall, seen through three slanted window frames">
        <defs>
          <linearGradient id="sepia" x1="0" y1="0" x2="1" y2="1">
            <stop offset="0" stop-color="var(--sepia-light)"/>
            <stop offset=".5" stop-color="var(--sepia-mid)"/>
            <stop offset="1" stop-color="var(--sepia-dark)"/>
          </linearGradient>
        </defs>
        <polygon points="6,20 52,4 96,214 58,222" fill="url(#sepia)" stroke="var(--frame)" stroke-width="4" stroke-linejoin="round"/>
        <polygon points="90,8 150,4 156,220 112,222" fill="url(#sepia)" stroke="var(--frame)" stroke-width="4" stroke-linejoin="round"/>
        <polygon points="186,4 244,8 214,222 170,216" fill="url(#sepia)" stroke="var(--frame)" stroke-width="4" stroke-linejoin="round"/>
      </svg>
      <p class="praise">"This is a novel to be read in one go.<br>A charming narrative…and unexpected turns.<br>It keeps the reader in constant suspense".</p>
      <p class="praise-source">Grafima Monthly Literary Review</p>
      <div class="imprint">Quillstone Books</div>
    </section>
  </main>
</body>
</html>
```